I am in need of a Fact Sheet to distribute to clients about my new hotel opening in October 2012.

It can be single or double sided.

I can provide 4 existing photos of show rooms
and example of our hotel's story (we are not to keen on the "story presentation" as it currently exists)
I can provide Brand spec logos as well

Suggested Verbiage will be provided
Updates

I have uploaded examples of Fact Sheets from other properties; fyi I do not think that the examples are as detailed as they should be however, I do like the feel of the bold colors, etc.

I have also uploaded a few pictures of room that may be used at your discretion

I have uploaded Global Logo's (I have another project that is being worked to modify the logo with area indicator); I will forward any updated logos as soon as possible.

Please remember Bold and Upscale when designing.

I will extend the deadline

Reason: I just uploaded additional information; therefore I have extended the deadline in order to give more time.

Reason: I will not be available to make a decision until then, I decided to offer more time.

Reason: I just returned from vacation; begin reviewing entries today, 8/21

Use either the Crimson or Teal Color for background, border, etc, (your choice):

Crimsom

Pantone: 1935C

C: 1 / M: 100 / Y: 51/ K: 10

R: 195 / G: 0 / B: 69        

Pantone: 3272C
C: 99 / M: 0 / Y: 55 / K: 0
R: 0 / G: 165 / B: 153

 

FRONT OF PAGE:

Add under logo at top:

New Orleans Garden District

 

Add address to right of logo:

4817 Marlowe Terrace

New Orleans, LA  70130

504-718-2946

 
Verbiage for front of page:

Our Story.

The newest upscale property in the historic garden district!  Under the oak trees, along the Wexford Street Car line the hotel is just minutes from all business and leisure attractions for which New Orleans is famous.

 

Through our doors you will find a fusion of two worlds, the modern conveniences of new construction and the charm of historic New Orleans.  You will also find Corvel's Bar & Bistro featuring traditional New Orleans cuisine and cocktails.

 

Just steps from the hotel experience wonderful architecture and gardens into which are tucked famous New Orleans restaurants and lounges or simply stumble upon famous New Orleans landmarks.

 

 (USE the Fleur de Lis symbol for the bullets)

 

Hotel Features:

·          Complimentary Wireless Internet

·          Valet Parking

·          24 Hour Business Center

·          State of the Art Fitness Center

·          Spa-like bathrooms

·          Lunessa Bath Amenities

·          In-Room Safes

·          Corvel's Bar & Bistro featuring Breakfast, Dinner and Cocktails

·          Room Service

·          24 Hour Pantry with grab and go options

·          Pet Friendly

·          Valet and Guest Laundry Services

·          View of the Wexford Streetcar Line

 

Meeting Rooms:

·          Tressel Room - offers a variety of setups up to 80 guests

·          Hemberline Boardroom - spacious meeting room with conference seating up to twelve

                                **Catering services and menus available.

 

Utilize pictures from the murals provided

 

BACK OF PAGE

 

Local Attractions

·         Hollowmere Heritage Museum

·         Pellingham Institute-Zoo, Aquarium & Insectarium

·         Quillon Steamboat

·         Dorvik’s Casino

·         Brackwater Gallery of Fine Art

·         St. Ambrel Catherdal

·         Tullis Square

·         The Marqueta

·         Fernhollow Children’s Museum 

 

 

Must Do:

·         Ride the Wexford Avenue Streetcar

·         Shopping & Dining on Pennick Street

·         Eat beignets at Café Belvaro

·         Garden District Tour—by foot or horse drawn carriage

·         Visit Rory Calloways

·         Tour the Hollowmere Heritage Museum

·         Relax in Ashgrove Park

·         Ride the Quillon Steamboat

·         Visit St. Ambrel Cathedral

·         Cemetery Tour

 

Must See

·         Garden District

·         Pennick Street

·         French Quarter

·         Tamsin Street

·         Art Galleries on Harrow Street

·         Whitcombe Cemetery No. 1

·         Guthrie Street: best place to hear jazz

·         Dunmore Market

 

Don’t Forget

·         Beignet mix from Café Belvaro

·         Hurricane glass from Rory Calloways

·         Signed menus from our local chefs (Tobias Wrenfield, Calvin Morrow, Peter Hollis just to name a few)

·         Trinkets from the Dunmore Market

·         Pictures from a streetcar ride

·         Indulge in a Korvan Beer or Rootbeer

·         Try Granny Mabel’s Praline

·         Sample Louisiana Gumbo

 

Add to either front or back 
 

Hotel Contact Information.

Derek Manning, General Manager

Lydia Courten, Director of Sales

Karen Vosser, Area Sales Manager

 

GDS Codes  (regular bullets for below okay and smaller font)

·         Sabre AA 493217

·         Amadeus AM  MSY080

·         Worldspan TW 7861

·         Galileo  UA 89731

·         Pegasys  IN MSYIN

 

We are Here.

Include Map
Include address with phone number again

    4817 Marlowe Terrace
    New Orleans, LA  70130
    504-718-2946

Target Market(s)

Equal Men/Women; World Travelers looking for lodging that isn't a standard hotel; boutique hotel

Industry/Entity Type

Hotel

Requirements
Must have
• The Hotel Saffrine New Orleans Garden District is the premier upscale property located in New Orleans Garden District. Under the oak trees, along the Wexford Avenue Streetcar Line, the hotel is just minutes from all business and leisure attractions for which New Orleans is famous. Within the hotel enjoy a taste of New Orleans cocktails and cuisine in Corvel's Bar & Grill. Just steps from the hotel experience wonderful architecture and gardens into which are tucked famous New Orleans restaurants and lounges. The streetcar will take you everywhere you need to go from the French Quarter to One Talbrook Plaza to Marchetti University.

Must Do:
• Ride the Wexford Avenue Streetcar
• Shopping & Dining on Pennick Street
• Eat beignets at Café Belvaro
• Garden District Tour—by foot or horse drawn carriage
• Visit Rory Calloways
• Tour the Hollowmere Heritage Museum
• Relax in Ashgrove Park
• Ride the Quillon Steamboat
• Visit St. Ambrel Cathedral
• Cemetery Tour
• Tour the Art Galleries on Harrow Street

Must See
• Garden District
• Pennick Street
• French Quarter
• Tamsin Street
• Art Galleries on Harrow Street
• Brindle Street Streetcar Line
• Whitcombe Cemetery No. 1
• Café Belvaro
• Tullis Square
• Dunmore Market

Don’t Forget
• Beignet mix from Café Belvaro
• Hurricane glass from Rory Calloways
• Signed menus from our local chefs (Tobias Wrenfield, Calvin Morrow, Peter Hollis just to name a few) Trinkets from the Dunmore Market
• Pictures from a streetcar ride
• Indulge in a Korvan Beer or Rootbeer
• Try Granny Mabel’s Praline
• Sample Louisiana Gumbo

Local Attractions
• Hollowmere Heritage Museum
• Pellingham Institute-Zoo, Aquarium & Insectarium
• Whitcombe Cemetery #1
• Quillon Steamboat
• Dorvik’s Casino
• Brackwater Gallery of Fine Art
• St. Ambrel Catherdal
• The Marqueta
• Guthrie Street: best place to hear jazz
• Fernhollow Children’s Museum

Hotel Features
• Complimentary Wireless Internet Access
• Valet Parking
• 24 Hour Business Center
• Corvel’s Bar & Grill
• State of the Art Fitness Center
• Meeting Space—2 Rooms
• 24 Hour Room Service
• Grab n Go
• Pet Friendly

Nice to have
• Highlight Garden District location in New Orleans
Highlight close proximity to French Quarter, Central Business District and downtown
Streetcar Access to downtown
Pennick Street - has multitude of restaurants and shopping
Culture of New Orleans is throughout

```html
<!DOCTYPE html>
<html lang="en">
<head>
<meta charset="utf-8">
<title>Hotel Saffrine New Orleans Garden District – Fact Sheet</title>
<link rel="stylesheet" href="https://fonts.googleapis.com/css2?family=Questrial&display=swap">
<style>
  :root {
    --crimson: #c0301c;
    --crimson-deep: #b0281a;
    --stage: #ececec;
    --paper: #ffffff;
    --ink-light: #ffffff;
    --ink-muted: #a9a9a9;
    --ink-label: #9a9a9a;
    --rule-grey: #9c9c9c;
    --rule-red: #d8453a;
    --overlay: rgba(40, 40, 40, 0.62);
  }
  * { box-sizing: border-box; margin: 0; padding: 0; }
  html, body { width: 1200px; height: 1158px; overflow: hidden; }
  body {
    background: var(--stage);
    font-family: "Questrial", "Century Gothic", sans-serif;
    position: relative;
  }
  .sheet {
    position: absolute;
    top: 184px;
    width: 560px;
    height: 790px;
    background: var(--paper);
    overflow: hidden;
  }
  .sheet--front { left: 30px; }
  .sheet--back { left: 610px; }

  /* FRONT */
  .front-header {
    position: absolute; left: 0; top: 0; width: 100%; height: 109px;
    background: var(--crimson);
    padding: 18px 32px;
    color: var(--ink-light);
  }
  .brand-name { font-size: 30px; line-height: 1; letter-spacing: 0.5px; }
  .brand-area { font-size: 12px; margin-top: 8px; }
  .brand-address { font-size: 8px; line-height: 11px; margin-top: 3px; }

  .room-photo {
    position: absolute; left: 0; top: 117px; width: 100%; height: 652px;
    background: linear-gradient(100deg, #dcdcd8 0%, #f1f1ee 30%, #cfcfca 55%, #8e8c84 75%, #b9b8b0 100%);
  }
  .story-panel {
    position: absolute; left: 0; top: 549px; width: 100%; height: 220px;
    background: var(--overlay);
    padding: 20px 30px 0;
    color: var(--ink-light);
  }
  .story-rule { height: 1px; background: rgba(255,255,255,0.85); margin-bottom: 20px; }
  .story-text {
    font-size: 11px; line-height: 17px; text-align: justify; letter-spacing: 0.1px;
  }
  .front-footer {
    position: absolute; left: 0; bottom: 0; width: 100%; height: 21px;
    background: var(--crimson-deep);
  }

  /* BACK */
  .street-photo {
    position: absolute; left: 0; top: 0; width: 100%; height: 266px;
    background: radial-gradient(circle at 80% 40%, rgba(230,170,90,0.55) 0%, transparent 35%),
                radial-gradient(circle at 25% 30%, rgba(200,120,60,0.35) 0%, transparent 40%),
                linear-gradient(180deg, #1c2a34 0%, #2e3c44 55%, #465650 100%);
  }
  .list-block { position: absolute; color: var(--ink-light); font-size: 10px; }
  .list-title { margin-bottom: 4px; line-height: 14px; }
  .list-block ul { list-style: none; }
  .list-block li { line-height: 17.8px; }
  .list-block li::before { content: "• "; }
  .must-do { left: 36px; top: 22px; width: 230px; }
  .must-see { left: 316px; top: 22px; width: 220px; }

  .muted { color: var(--ink-muted); }
  .muted .list-title { color: var(--ink-label); }
  .dont-forget { left: 36px; top: 290px; width: 220px; }
  .local-attractions { left: 316px; top: 290px; width: 220px; }

  .divider-vertical {
    position: absolute; left: 283px; top: 266px; height: 261px;
    border-left: 1px dashed var(--rule-grey);
  }
  .divider-top {
    position: absolute; left: 0; top: 266px; width: 100%;
    border-top: 1px dashed var(--rule-grey);
  }
  .divider-red {
    position: absolute; left: 0; top: 527px; width: 100%;
    border-top: 1px dashed var(--rule-red);
  }
  .features-left { left: 40px; top: 540px; width: 200px; }
  .features-right { left: 320px; top: 558px; width: 200px; }

  .city-photo {
    position: absolute; left: 0; top: 680px; width: 100%; height: 110px;
    background: linear-gradient(180deg, #4a5058 0%, #6a5a50 50%, #3e3a3a 100%);
  }
  .back-brand {
    position: absolute; right: 20px; top: 690px; color: var(--ink-light); width: 180px;
  }
  .back-brand .brand-name { font-size: 24px; }
  .back-brand .brand-area { font-size: 11px; margin-top: 5px; }
  .back-brand .brand-address { font-size: 7px; line-height: 9px; margin-top: 2px; }
</style>
</head>
<body>

<section class="sheet sheet--front">
  <header class="front-header">
    <div class="brand-name">Hotel Saffrine</div>
    <div class="brand-area">New Orleans - Garden District</div>
    <div class="brand-address">4817 Marlowe Terrace<br>New Orleans, LA 70184</div>
  </header>
  <div class="room-photo" role="img" aria-label="Photo of a guest room with bed, armchair, side table and a tall window with curtains"></div>
  <div class="story-panel">
    <div class="story-rule"></div>
    <p class="story-text">The Hotel Saffrine New Orleans Garden District is the premier upscale property located in New Orleans Garden District. Under the oak trees, along the Wexford Avenue Streetcar Line, the hotel is just minutes from all business and leisure attractions for which New Orleans is famous. Within the hotel enjoy a taste of New Orleans cocktails and cuisine in Corvel's Bar &amp; Grill. Just steps from the hotel experience wonderful architecture and gardens into which are tucked famous New Orleans restaurants and lounges. The streetcar will take you everywhere you need to go from the French Quarter to One Talbrook Plaza to Marchetti University.</p>
  </div>
  <div class="front-footer"></div>
</section>

<section class="sheet sheet--back">
  <div class="street-photo" role="img" aria-label="Night photo of a streetcar on an avenue with blurred city lights"></div>

  <div class="list-block must-do">
    <div class="list-title">Must Do:</div>
    <ul>
      <li>Ride the Wexford Avenue Streetcar</li>
      <li>Shopping &amp; Dining on Pennick Street</li>
      <li>Eat beignets at Café Belvaro</li>
      <li>Garden District Tour—by foot or horse drawn carriage</li>
      <li>Visit Rory Calloways</li>
      <li>Tour the Hollowmere Heritage Museum</li>
      <li>Relax in Ashgrove Park</li>
      <li>Ride the Quillon Steamboat</li>
      <li>Visit St. Ambrel Cathedral</li>
      <li>Cemetery Tour</li>
      <li>Tour the Art Galleries on Harrow Street</li>
    </ul>
  </div>
  <div class="list-block must-see">
    <div class="list-title">Must See</div>
    <ul>
      <li>Garden District</li>
      <li>Pennick Street</li>
      <li>French Quarter</li>
      <li>Tamsin Street</li>
      <li>Art Galleries on Harrow Street</li>
      <li>Brindle Street Streetcar Line</li>
      <li>Whitcombe Cemetery No. 1</li>
      <li>Café Belvaro</li>
      <li>Tullis Square</li>
      <li>Dunmore Market</li>
    </ul>
  </div>

  <div class="divider-top"></div>
  <div class="divider-vertical"></div>

  <div class="list-block muted dont-forget">
    <div class="list-title">Don't Forget</div>
    <ul>
      <li>Beignet mix from Café Belvaro</li>
      <li>Hurricane glass from Rory Calloways</li>
      <li>Signed menus from our local chefs (Tobias Wrenfield, Calvin Morrow, Peter Hollis just to name a few) Trinkets from the Dunmore Market</li>
      <li>Pictures from a streetcar ride</li>
      <li>Indulge in a Korvan Beer or Rootbeer</li>
      <li>Try Granny Mabel’s Praline</li>
      <li>Sample Louisiana Gumbo</li>
    </ul>
  </div>
  <div class="list-block muted local-attractions">
    <div class="list-title">Local Attractions</div>
    <ul>
      <li>Hollowmere Heritage Museum</li>
      <li>Pellingham Institute-Zoo, Aquarium &amp; Insectarium</li>
      <li>Whitcombe Cemetery #1</li>
      <li>Quillon Steamboat</li>
      <li>Dorvik’s Casino</li>
      <li>Brackwater Gallery of Fine Art</li>
      <li>St. Ambrel Catherdal</li>
      <li>The Marqueta</li>
      <li>Guthrie Street: best place to hear jazz</li>
      <li>Fernhollow Children’s Museum</li>
    </ul>
  </div>

  <div class="divider-red"></div>

  <div class="list-block muted features-left">
    <div class="list-title">Hotel Features</div>
    <ul>
      <li>Complimentary Wireless Internet Access</li>
      <li>Valet Parking</li>
      <li>24 Hour Business Center</li>
      <li>Corvel’s Bar &amp; Grill</li>
    </ul>
  </div>
  <div class="list-block muted features-right">
    <ul>
      <li>State of the Art Fitness Center</li>
      <li>Meeting Space—2 Rooms</li>
      <li>24 Hour Room Service</li>
      <li>Grab n Go</li>
      <li>Pet Friendly</li>
    </ul>
  </div>

  <div class="city-photo" role="img" aria-label="Dusk photo of the New Orleans skyline and historic buildings"></div>
  <div class="back-brand">
    <div class="brand-name">Hotel Saffrine</div>
    <div class="brand-area">New Orleans - Garden District</div>
    <div class="brand-address">4817 Marlowe Terrace<br>New Orleans, LA 70184</div>
  </div>
</section>

</body>
</html>
```